Hello,
We’re looking for a new WordPress website for Gather Your Light, our company offering unique well-being retreats and workshops.
We currently have a website online (you can consult it : www.gatheryourlight.ch), but we now need to build a new site on WordPress — more flexible, more intuitive to manage, and better aligned with our evolving needs.

What we’re looking for:
A new userfriendly WordPress site, with:
Inspiring, elegant, and modern design
Smooth user experience on desktop and mobile
Innovative design proposals – we want to be inspired !
SEO best practices
Respect of our existing color palette
The final website will need to be set up on our existing hosting provider (details can be shared later)

Pages to Include:
- Home
- Our Story
- Our Stays - with links to 5 individual pages, each describing one of our stays in detail.
- Activities – with potential links to individual descriptive pages
- Agenda
- Our Charter
- The Team
- Contact
- Blog

Required Features:
- Space for photos and videos
- Sections for testimonials and press articles
- Blog/article layout with strong readability
- Easy-to-update backend for future content
- Newsletter sign-up (pop-up and in footer)
- Additional pop-up on/off
- “Request info” buttons
- “Booking request” buttons
- Integration of our 4 pillars - Breathe · Feel · Connect · Experience - in the design (They’re currently in the footer, but we’re open to creative suggestions)

Who we are :
Gather Your Light offers well-being and personal growth stays but with a very different spirit.
We’re not a classic wellness brand. Our approach is professional, joyful, and grounded.
We create spaces where people can take a real break — breathe, slow down, and reconnect with themselves.
During our stays, people are welcomed like friends:
with warmth, respect, and no pressure.
Each program combines practices like breathwork, movement, creativity, coaching, and massages in a relaxed, beautiful setting of the French Alps.
What makes us different:
A friendly and down-to-earth atmosphere
A wide mix of activities.
A mix of inner work and simple pleasures
Private rooms, nourishing food, and shared moments
Time to talk, to laugh, to walk, or just be silent together - and feel free to be yourself
Our guests come to pause.
They leave feeling lighter, aligned, and full of life

```html
<!DOCTYPE html>
<html lang="fr">
<head>
<meta charset="utf-8">
<title>Gather Your Light – L'équipe</title>
<link href="https://fonts.googleapis.com/css2?family=Barlow:wght@400;500;600;700&family=Playfair+Display:wght@700&display=swap" rel="stylesheet">
<style>
:root{
  --navy:#1a3d99;
  --navy-deep:#0f2868;
  --teal:#6cc2bd;
  --teal-dark:#3e8f8c;
  --teal-pale:#c9ebe8;
  --ink:#333a45;
  --line:#d9dde4;
  --white:#ffffff;
}
*{box-sizing:border-box;margin:0;padding:0}
html,body{width:1200px;height:3140px;overflow:hidden}
body{position:relative;background:var(--white);font-family:"Barlow",sans-serif;color:var(--ink)}
a{color:inherit}

.topbar{position:absolute;left:0;top:0;width:1200px;height:39px;background:var(--navy);color:var(--white);font-size:12px}
.topbar .contact{position:absolute;left:141px;top:0;height:39px;display:flex;align-items:center;gap:22px}
.topbar .contact span{display:flex;align-items:center;gap:8px}
.topbar .actions{position:absolute;right:140px;top:0;display:flex;gap:10px}
.topbar .actions a{display:block;height:39px;line-height:39px;padding:0 15px;font-size:12.5px;text-decoration:none}
.btn-info{background:var(--teal-pale);color:var(--navy)}
.btn-book{background:var(--teal);color:var(--white)}

.header{position:absolute;left:0;top:39px;width:1200px;height:73px;background:var(--white)}
.brand{position:absolute;left:141px;top:0;height:73px;display:flex;align-items:center;gap:10px;font-weight:700;font-size:22px;color:var(--navy);letter-spacing:1px}
.brand i{display:block;width:14px;height:14px;border-radius:50%;background:var(--teal)}
.nav{position:absolute;right:141px;top:0;height:73px;display:flex;align-items:center;gap:28px;font-size:13px;color:var(--navy)}
.nav .active{color:#222}

.hero{position:absolute;left:0;top:112px;width:1200px;height:460px;overflow:hidden}
.hero-photo{position:absolute;inset:0;background:radial-gradient(circle at 58% 45%,#f5d9a0 0%,#c89a5c 18%,#6c6252 42%,#3b4038 70%,#22281f 100%)}
.hero h1{position:absolute;left:141px;top:118px;font-family:"Playfair Display",serif;font-size:52px;color:var(--white);letter-spacing:1px}
.crumbs{position:absolute;left:142px;top:190px;display:flex;align-items:center;gap:10px;color:var(--white);font-size:15px}
.crumbs b{font-size:12px;font-weight:600}
.hero-band{position:absolute;left:0;bottom:0;width:1200px;height:8px;background:var(--teal)}

.posts{position:absolute;left:141px;top:671px;width:918px;display:grid;grid-template-columns:repeat(3,283px);column-gap:35px;row-gap:36px}
.post{height:425px;border:1px solid var(--line);border-radius:8px;overflow:hidden;background:var(--white);position:relative}
.post .thumb{height:253px}
.post .date{position:absolute;left:14px;top:231px;height:24px;line-height:24px;padding:0 9px;font-size:13px;font-weight:600;color:var(--white);background:var(--navy);border-radius:2px}
.post .date.alt{background:var(--teal)}
.post h2{margin:24px 14px 0;font-size:18px;font-weight:500;color:var(--navy)}
.post p{margin:8px 14px 0;width:240px;font-size:11.5px;line-height:22.5px;color:#444}
.post a{display:block;margin:14px 14px 0;font-size:12px;font-weight:500;color:var(--navy);text-decoration:underline}

.pager{position:absolute;left:465px;top:2056px;display:flex;align-items:center;gap:9px}
.pager span{width:29px;height:29px;border:1px solid var(--line);display:flex;align-items:center;justify-content:center;font-size:13px;color:#555;border-radius:2px}
.pager span.current{background:var(--navy);border-color:var(--navy);color:var(--white)}
.pager .arrow{border:none;width:30px}

.pillars{position:absolute;left:141px;top:2164px;display:flex;gap:23px}
.pillar{width:212px;height:247px;border-radius:12px;color:var(--white);text-align:center;padding:28px 12px 0}
.pillar h3{font-size:19px;font-weight:500;margin-top:10px}
.pillar p{font-size:12px;line-height:19px;margin-top:14px}
.p1{background:var(--teal)}
.p2{background:var(--teal-dark)}
.p3{background:var(--navy)}
.p4{background:linear-gradient(180deg,#143584,var(--navy-deep))}

.footer{position:absolute;left:0;top:2490px;width:1200px;height:650px;color:var(--white)}
.footer-bg{position:absolute;left:0;top:150px;width:1200px;height:500px;background:var(--navy)}
.footer-band{position:absolute;left:0;top:142px;width:1200px;height:8px;background:var(--teal)}
.footer-brand{position:absolute;left:265px;top:230px;font-size:40px;font-weight:700;letter-spacing:2px;line-height:1.1}
.booking{position:absolute;left:587px;top:225px}
.booking h4{font-size:24px;font-weight:500}
.booking .row{display:flex;align-items:center;gap:14px;margin-top:12px}
.booking .reserve{background:var(--teal);color:var(--white);font-size:23px;padding:4px 22px;border-radius:22px}
.booking .phone{display:flex;align-items:center;gap:8px;font-size:24px;font-weight:500}
.rule{position:absolute;left:141px;width:918px;height:1px;background:rgba(255,255,255,.25)}
.fcol{position:absolute;top:403px}
.fcol h5{font-size:16px;font-weight:600;letter-spacing:.3px}
.fcol ul{list-style:none;margin-top:14px;font-size:12px;line-height:23px}
.links{display:flex;gap:60px}
.newsletter p{font-size:11.5px;line-height:19px;margin-top:12px;width:370px}
.subscribe{display:flex;margin-top:12px;width:375px;height:38px;border:1px solid var(--white);border-radius:20px;overflow:hidden}
.subscribe span{flex:1;padding-left:16px;line-height:36px;font-size:11.5px}
.subscribe b{background:var(--teal);padding:0 12px;line-height:36px;font-size:14px;font-weight:500}
.copy{position:absolute;left:0;width:1200px;top:605px;text-align:center;font-size:12px}
</style>
</head>
<body>

<div class="topbar">
  <div class="contact">
    <span><svg width="16" height="16" viewBox="0 0 24 24" fill="none" stroke="#fff" stroke-width="2"><path d="M5 3h4l2 5-3 2a11 11 0 0 0 6 6l2-3 5 2v4a2 2 0 0 1-2 2A17 17 0 0 1 3 5a2 2 0 0 1 2-2z"/></svg>+41 58 200 74 26</span>
    <span><svg width="20" height="14" viewBox="0 0 20 14" fill="none" stroke="#fff" stroke-width="1.6"><rect x="1" y="1" width="18" height="12"/><path d="M1 1l9 7 9-7"/></svg>info@gatheryourlight.ch</span>
  </div>
  <div class="actions">
    <a class="btn-info" href="#">Demande d'information</a>
    <a class="btn-book" href="#">Demande de réservation</a>
  </div>
</div>

<header class="header">
  <div class="brand"><i></i>GATHER YOUR LIGHT</div>
  <nav class="nav">
    <span>Accueil</span><span>Notre histoire</span><span>Nos séjours</span><span>Activités</span><span>Ordre du jour</span><span>Notre charte</span><span class="active">Blogue</span><span>Contact</span>
  </nav>
</header>

<section class="hero">
  <div class="hero-photo" role="img" aria-label="Photo d'une fleur de pissenlit devant un coucher de soleil entre les sapins"></div>
  <h1>L'EQUIPE</h1>
  <div class="crumbs">Home <span>»</span> <b>Blogue</b></div>
  <div class="hero-band"></div>
</section>

<main class="posts">
  <article class="post"><div class="thumb" role="img" aria-label="Photo de deux femmes se serrant la main à l'accueil" style="background:linear-gradient(135deg,#f1efea,#c9b9a6 60%,#7c4a36)"></div><span class="date">05 July 2025</span><h2>Existe de nombreuses</h2><p>Contrairement à la croyance populaire, le Lorem Ipsum n'est pas un simple texte aléatoire Il trouve ses origines dans.</p><a href="#">Apprendre encore plus</a></article>
  <article class="post"><div class="thumb" role="img" aria-label="Photo d'une chambre avec un lit double" style="background:linear-gradient(160deg,#e9e9ea,#cfcdcb 55%,#8b7a6a)"></div><span class="date alt">15 July 2025</span><h2>Existe de nombreuses</h2><p>Contrairement à la croyance populaire, le Lorem Ipsum n'est pas un simple texte aléatoire Il trouve ses origines dans.</p><a href="#">Apprendre encore plus</a></article>
  <article class="post"><div class="thumb" role="img" aria-label="Photo d'une femme soufflant sur un pissenlit dans un pré" style="background:linear-gradient(135deg,#2f4a2a,#6d8a4e 55%,#c9cfbf)"></div><span class="date">20 July 2025</span><h2>Existe de nombreuses</h2><p>Contrairement à la croyance populaire, le Lorem Ipsum n'est pas un simple texte aléatoire Il trouve ses origines dans.</p><a href="#">Apprendre encore plus</a></article>
  <article class="post"><div class="thumb" role="img" aria-label="Photo d'une assiette gastronomique en plein air" style="background:linear-gradient(135deg,#6f8f3a,#c7cfd6 55%,#dcd37a)"></div><span class="date">25 July 2025</span><h2>Existe de nombreuses</h2><p>Contrairement à la croyance populaire, le Lorem Ipsum n'est pas un simple texte aléatoire Il trouve ses origines dans.</p><a href="#">Apprendre encore plus</a></article>
  <article class="post"><div class="thumb" role="img" aria-label="Photo d'un salon de chalet avec cheminée" style="background:linear-gradient(135deg,#8a5b3a,#6b6a64 55%,#b9a94a)"></div><span class="date alt">25 July 2025</span><h2>Existe de nombreuses</h2><p>Contrairement à la croyance populaire, le Lorem Ipsum n'est pas un simple texte aléatoire Il trouve ses origines dans.</p><a href="#">Apprendre encore plus</a></article>
  <article class="post"><div class="thumb" role="img" aria-label="Photo d'un sauna en bois" style="background:linear-gradient(135deg,#d8ccb8,#bfae94 55%,#3a4448)"></div><span class="date">25 July 2025</span><h2>Existe de nombreuses</h2><p>Contrairement à la croyance populaire, le Lorem Ipsum n'est pas un simple texte aléatoire Il trouve ses origines dans.</p><a href="#">Apprendre encore plus</a></article>
  <article class="post"><div class="thumb" role="img" aria-label="Photo d'une mère et sa fille arrosant un jardin" style="background:linear-gradient(135deg,#4f6a2c,#a34535 55%,#d9c7a8)"></div><span class="date">20 July 2025</span><h2>Existe de nombreuses</h2><p>Contrairement à la croyance populaire, le Lorem Ipsum n'est pas un simple texte aléatoire Il trouve ses origines dans.</p><a href="#">Apprendre encore plus</a></article>
  <article class="post"><div class="thumb" role="img" aria-label="Photo d'une suite d'hôtel avec salon" style="background:linear-gradient(135deg,#6f7378,#a78f70 55%,#3d332b)"></div><span class="date alt">05 July 2025</span><h2>Existe de nombreuses</h2><p>Contrairement à la croyance populaire, le Lorem Ipsum n'est pas un simple texte aléatoire Il trouve ses origines dans.</p><a href="#">Apprendre encore plus</a></article>
  <article class="post"><div class="thumb" role="img" aria-label="Photo d'une main tenant un pissenlit dans un champ" style="background:linear-gradient(160deg,#dfe6df,#9cab7c 55%,#7a8a4c)"></div><span class="date">15 July 2025</span><h2>Existe de nombreuses</h2><p>Contrairement à la croyance populaire, le Lorem Ipsum n'est pas un simple texte aléatoire Il trouve ses origines dans.</p><a href="#">Apprendre encore plus</a></article>
</main>

<nav class="pager">
  <span class="arrow"><svg width="10" height="16" viewBox="0 0 10 16" fill="none" stroke="#888" stroke-width="2"><path d="M8 2L2 8l6 6"/></svg></span>
  <span class="current">1</span><span>2</span><span>3</span><span>4</span><span>5</span>
  <span class="arrow"><svg width="10" height="16" viewBox="0 0 10 16" fill="none" stroke="#222" stroke-width="2"><path d="M2 2l6 6-6 6"/></svg></span>
</nav>

<section class="pillars">
  <div class="pillar p1">
    <svg width="48" height="52" viewBox="0 0 48 52" fill="none" stroke="#fff" stroke-width="1.6"><circle cx="22" cy="16" r="11"/><path d="M14 26c-2 10 0 18 4 24M30 26c2 10 0 18-4 24M36 12l6-3M37 18h6"/></svg>
    <h3>Respirer</h3>
    <p>Profondément et offrez-vous le luxe de ralentir. Nos programmes sont pensés pour que chaque participant puisse renouer...</p>
  </div>
  <div class="pillar p2">
    <svg width="52" height="52" viewBox="0 0 52 52" fill="none" stroke="#fff" stroke-width="1.6"><ellipse cx="26" cy="8" rx="9" ry="3"/><path d="M26 48C10 38 6 30 6 24a10 10 0 0 1 20-2 10 10 0 0 1 20 2c0 6-4 14-20 24z"/></svg>
    <h3>Ressentez</h3>
    <p>Chaque sensation, chaque émotion. Grâce à une approche holistique enrichie par des intervenants passionnés,...</p>
  </div>
  <div class="pillar p3">
    <svg width="52" height="52" viewBox="0 0 52 52" fill="none" stroke="#fff" stroke-width="1.6"><path d="M26 6c6 6 6 16 0 22-6-6-6-16 0-22zM26 28c-8-2-14-8-16-14 8 0 14 6 16 14zM26 28c8-2 14-8 16-14-8 0-14 6-16 14z"/><circle cx="26" cy="36" r="5"/><path d="M14 48c2-6 6-8 12-8s10 2 12 8z"/></svg>
    <h3>Connectez</h3>
    <p>Pleinement, en petit groupe, dans un cadre chaleureux, humain et respectueux, avec des personnes partageant la même recherche...</p>
  </div>
  <div class="pillar p4">
    <svg width="56" height="52" viewBox="0 0 56 52" fill="none" stroke="#fff" stroke-width="1.6"><circle cx="28" cy="18" r="5"/><path d="M28 24v12M16 30c6 0 10 4 12 10 2-6 6-10 12-10M8 44c8-2 14-2 20 4 6-6 12-6 20-4M18 6l2 4M38 6l-2 4M10 14l4 2M46 14l-4 2M28 2v5"/></svg>
    <h3>Experience</h3>
    <p>le changement en profondeur et la richesse de chaque découverte. En explorant de nouvelles pratiques et en vous ouvrant...</p>
  </div>
</section>

<footer class="footer">
  <div class="footer-band"></div>
  <div class="footer-bg"></div>
  <div class="footer-brand">GATHER YOUR<br>LIGHT</div>
  <div class="booking">
    <h4>DEMANDE DE RÉSERVATION</h4>
    <div class="row">
      <span class="reserve">Réserver</span>
      <span class="phone"><svg width="24" height="24" viewBox="0 0 24 24" fill="none" stroke="#fff" stroke-width="2"><path d="M5 3h4l2 5-3 2a11 11 0 0 0 6 6l2-3 5 2v4a2 2 0 0 1-2 2A17 17 0 0 1 3 5a2 2 0 0 1 2-2z"/></svg>+41 58 200 74 26</span>
    </div>
  </div>
  <div class="rule" style="top:348px"></div>
  <div class="fcol" style="left:143px">
    <h5>LIENS RAPIDES</h5>
    <div class="links">
      <ul><li>Accueil</li><li>Notre histoire</li><li>Nos séjours</li><li>Activités</li></ul>
      <ul><li>Ordre du jour</li><li>Notre charte</li><li>Blog</li></ul>
    </div>
  </div>
  <div class="fcol" style="left:462px">
    <h5>SOUTIEN</h5>
    <ul><li>Contactez-nous</li><li>FAQ</li><li>Politique de confidentialité</li><li>Conditions d'utilisation</li></ul>
  </div>
  <div class="fcol newsletter" style="left:692px">
    <h5>INSCRIPTION AU BULLETIN D'INFORMATION</h5>
    <p>Inscrivez-vous à notre lettre d'information pour recevoir les dernières mises à jour dans votre boîte aux lettres électronique.</p>
    <div class="subscribe"><span>Adresse électronique</span><b>S'ABONNER</b></div>
  </div>
  <div class="rule" style="top:582px"></div>
  <div class="copy">© 2025 GATHER YOUR LIGHT. Tous droits réservés.</div>
</footer>

</body>
</html>
```